Business Card Design

Business Card for professional consulting firm working with large financial institutions.

Target Market(s)

Executive buyers

Industry/Entity Type

Banking

Contact Information for Business Card

Mild creativity wanted. Not boring, but do elaborate artwork.

Font styles to use
Serif
Sans Serif

Colors

Designer to choose colors to be used in the design.

Requirements
Must have
• Standard business card features - company name, individual name, telephone, website, email, locations.
Nice to have
• Two colors
Should not have
• too many colors, fancy printing, cartoons.

```html
<!DOCTYPE html>
<html lang="en">
<head>
<meta charset="utf-8">
<title>Northvale Advisory – Business Card</title>
<link href="https://fonts.googleapis.com/css2?family=Arimo:wght@400&family=Tinos:wght@400&display=swap" rel="stylesheet">
<style>
  :root {
    --bg: #262626;
    --paper: #ffffff;
    --red: #c41e1e;
    --black: #141414;
    --ink: #2b2b2b;
    --sans: "Arimo", Arial, sans-serif;
    --serif: "Tinos", "Times New Roman", serif;
  }
  html, body {
    margin: 0;
    width: 1200px;
    height: 1200px;
    overflow: hidden;
    background: var(--bg);
  }
  .canvas {
    position: relative;
    width: 1200px;
    height: 1200px;
  }
  .card {
    position: absolute;
    left: 127px;
    width: 945px;
    height: 540px;
    background: var(--paper);
    overflow: hidden;
    box-shadow: 0 10px 30px rgba(0,0,0,.45);
  }
  .card--front { top: 40px; }
  .card--back { top: 620px; }
  .card__art {
    position: absolute;
    inset: 0;
    width: 100%;
    height: 100%;
  }
  .art-red { fill: var(--red); }
  .art-black { fill: var(--black); }
  .art-white { fill: var(--paper); }

  .person-name {
    position: absolute;
    left: 330px;
    top: 52px;
    margin: 0;
    font-family: var(--sans);
    font-size: 46px;
    font-weight: 400;
    color: var(--red);
    line-height: 1;
  }
  .name-rule {
    position: absolute;
    left: 318px;
    top: 116px;
    width: 590px;
    height: 4px;
    background: var(--red);
  }
  .contact-list {
    position: absolute;
    left: 372px;
    top: 160px;
    margin: 0;
    padding: 0;
    list-style: none;
  }
  .contact-item {
    display: flex;
    align-items: center;
    height: 66px;
    font-family: var(--sans);
    font-size: 27px;
    color: var(--red);
  }
  .contact-icon {
    width: 44px;
    height: 44px;
    margin-right: 32px;
    flex: none;
  }
  .company-name {
    position: absolute;
    left: 440px;
    top: 222px;
    width: 470px;
    margin: 0;
    text-align: center;
    font-family: var(--serif);
    font-size: 58px;
    font-weight: 400;
    color: var(--ink);
    line-height: 1.1;
  }
</style>
</head>
<body>
<main class="canvas">

  <section class="card card--front" aria-label="Business card front">
    <svg class="card__art" viewBox="0 0 945 540" aria-hidden="true">
      <path class="art-red" d="M0,0 H180 C80,170 90,400 240,540 H0 Z"/>
      <path class="art-black" d="M180,0 H290 C180,150 190,400 360,540 H240 C90,400 80,170 180,0 Z"/>
      <path class="art-black" d="M945,40 C860,110 850,220 945,310 Z"/>
      <path class="art-white" d="M945,70 C880,130 875,210 945,280 Z"/>
      <path class="art-red" d="M945,95 C900,140 898,200 945,250 Z"/>
    </svg>

    <h1 class="person-name">Name</h1>
    <div class="name-rule"></div>

    <ul class="contact-list">
      <li class="contact-item">
        <svg class="contact-icon" viewBox="0 0 44 44" aria-hidden="true">
          <path d="M4,22 L22,6 L40,22" fill="none" stroke="#c41e1e" stroke-width="3.5"/>
          <rect x="10" y="20" width="24" height="19" fill="none" stroke="#c41e1e" stroke-width="3.5"/>
          <rect x="19" y="28" width="7" height="11" fill="#c41e1e"/>
        </svg>
        <span>address</span>
      </li>
      <li class="contact-item">
        <svg class="contact-icon" viewBox="0 0 44 44" aria-hidden="true">
          <rect x="4" y="10" width="36" height="24" fill="#c41e1e"/>
          <path d="M4,10 L22,25 L40,10" fill="none" stroke="#fff" stroke-width="2.5"/>
        </svg>
        <span>name@northvale.com</span>
      </li>
      <li class="contact-item">
        <svg class="contact-icon" viewBox="0 0 44 44" aria-hidden="true">
          <path d="M5,16 C5,6 39,6 39,16 L33,19 L29,14 H15 L11,19 Z" fill="#c41e1e"/>
          <rect x="9" y="21" width="26" height="17" rx="3" fill="#c41e1e"/>
          <circle cx="22" cy="29" r="4.5" fill="#fff"/>
        </svg>
        <span>012-345-678</span>
      </li>
      <li class="contact-item">
        <svg class="contact-icon" viewBox="0 0 44 44" aria-hidden="true">
          <g fill="none" stroke="#c41e1e" stroke-width="2.5">
            <circle cx="22" cy="22" r="18"/>
            <ellipse cx="22" cy="22" rx="8" ry="18"/>
            <line x1="4" y1="22" x2="40" y2="22"/>
            <line x1="22" y1="4" x2="22" y2="40"/>
            <path d="M7,13 H37 M7,31 H37"/>
          </g>
        </svg>
        <span>www.example.com</span>
      </li>
    </ul>
  </section>

  <section class="card card--back" aria-label="Business card back">
    <svg class="card__art" viewBox="0 0 945 540" aria-hidden="true">
      <path class="art-red" d="M0,0 H330 C200,150 150,360 190,540 H0 Z"/>
      <path class="art-black" d="M330,0 H420 C280,130 230,340 300,540 H190 C150,360 200,150 330,0 Z"/>
      <path class="art-red" d="M420,0 H560 C430,80 380,190 380,270 C350,180 370,90 420,0 Z"/>
      <path class="art-white" d="M520,0 H560 C440,70 395,160 385,240 C380,160 430,70 520,0 Z"/>
    </svg>
    <h2 class="company-name">Northvale Advisory</h2>
  </section>

</main>
</body>
</html>
```